Environmental Health Survey for Medical Providers in Indiana

I am sending out an environmental health survey to all health care providers (MDs, NPs, and DOs) in Indiana to assess their knowledge of environmental health concerns that effect their patients. Based on that assessment, I will then send them targeted free continuing education modules to bolster their knowledge in any weak points. The postcard will have a website link on it that they will go to for the survey (I wish I could email them, but Indiana doesn't collect provider emails, only addresses). I need to somehow pull these providers in to complete my survey and get the free CEs. This is for my doctorate thesis. The survey link is: http://shortlinkr.example/surveyquo

Target Market(s)

Nurse Practitioners, Medical Doctors, and Doctors of Osteopathic Medicine in Indiana.

Industry/Entity Type

Health Care

Colors
00a990
33b8a4

Requirements
Must have
• 1. A space for addresses & postage, as these will be mailed.
• 2. The survey link

```html
<!DOCTYPE html>
<html lang="en">
<head>
<meta charset="utf-8">
<title>Environmental Health Survey – Executive Summary and Postcard</title>
<link rel="stylesheet" href="https://fonts.googleapis.com/css2?family=Cabin:wght@400;600;700&family=PT+Sans:wght@400;700&display=swap">
<style>
:root{
  --red:#b0222f;
  --red-dark:#8e1a25;
  --red-light:#d13b47;
  --ink:#4a4a4a;
  --ink-soft:#5c5c5c;
  --panel:#eeeeef;
  --paper:#ffffff;
  --stage:#dcdcdc;
  --line:#b9b9b9;
}
*{box-sizing:border-box;margin:0;padding:0}
html,body{width:1200px;height:723px;overflow:hidden}
body{background:var(--stage);position:relative;font-family:"Cabin",sans-serif;color:var(--ink)}

/* ---------- Executive summary sheet ---------- */
.summary-sheet{position:absolute;left:65px;top:38px;width:425px;height:624px;background:var(--panel);box-shadow:0 2px 8px rgba(0,0,0,.25);overflow:hidden}
.summary-art{position:absolute;left:0;top:0;width:425px;height:250px}
.brand{position:absolute;display:flex;align-items:center;gap:7px;font-family:"Cabin",sans-serif;font-size:17px;color:var(--ink-soft);font-weight:400}
.brand-mark{width:13px;height:13px;background:var(--red);flex:none}
.summary-sheet .brand{left:11px;top:19px}
.summary-title{position:absolute;left:10px;top:58px;font-family:"Cabin",sans-serif;font-weight:400;font-size:27px;line-height:34px;color:var(--red);letter-spacing:.5px}
.summary-body{position:absolute;left:15px;top:228px;width:396px;font-size:10.3px;line-height:11.6px;color:var(--ink);text-align:justify;hyphens:auto}
.summary-body p{margin-bottom:7px}
.survey-pill{position:absolute;left:15px;top:577px;width:394px;height:31px;border-radius:16px;background:linear-gradient(90deg,var(--red-light),var(--red) 60%,var(--red-dark));color:#fff;font-size:14px;line-height:31px;text-align:center}
.survey-pill strong{font-weight:700}

/* ---------- Postcard ---------- */
.postcard{position:absolute;left:520px;top:238px;width:625px;height:425px;background:var(--paper);box-shadow:0 2px 8px rgba(0,0,0,.25);overflow:hidden}
.postcard-art{position:absolute;left:0;top:0;width:625px;height:425px}
.topics{position:absolute;left:18px;top:25px;font-family:"PT Sans",sans-serif}
.topics h2{font-family:"Cabin",sans-serif;font-weight:400;font-size:14.5px;color:var(--red);margin-bottom:3px}
.topics ul{list-style:none}
.topics li{display:flex;align-items:center;gap:6px;font-size:10.7px;line-height:15.9px;color:var(--ink)}
.topics li svg{flex:none}
.ce-links{position:absolute;left:18px;top:300px;color:#fff;font-family:"PT Sans",sans-serif}
.ce-links h3{font-size:11px;font-weight:700;margin-bottom:2px}
.ce-links p{font-size:9px;line-height:11px}
.card-survey{position:absolute;left:15px;top:391px;font-size:11.5px;color:var(--red)}
.card-survey strong{font-weight:700}
.postcard .brand{left:330px;top:29px}
.stamp-box{position:absolute;left:532px;top:24px;width:66px;height:50px;border:1px solid var(--line)}
.address-lines{position:absolute;left:422px;top:165px;width:176px}
.address-lines span{display:block;height:29px;border-bottom:1px solid var(--line)}
</style>
</head>
<body>

<section class="summary-sheet" aria-label="Executive summary">
  <svg class="summary-art" viewBox="0 0 425 250" aria-hidden="false">
    <defs>
      <linearGradient id="photoTone" x1="0" y1="0" x2="1" y2="1">
        <stop offset="0" stop-color="#cfe3f2"/>
        <stop offset=".55" stop-color="#6fa3cf"/>
        <stop offset="1" stop-color="#2f5f93"/>
      </linearGradient>
      <linearGradient id="swooshRed" x1="0" y1="0" x2="1" y2="0">
        <stop offset="0" stop-color="#d13b47"/>
        <stop offset="1" stop-color="#9c1c28"/>
      </linearGradient>
    </defs>
    <rect width="425" height="250" fill="#ffffff"/>
    <g role="img" aria-label="Photo of a smiling nurse in blue scrubs with a stethoscope, colleagues behind her">
      <path d="M232 0 H425 V176 Q350 222 262 190 Q205 160 205 95 Q205 35 232 0Z" fill="url(#photoTone)"/>
    </g>
    <path d="M0 178 Q110 185 220 205 Q330 225 425 170 V192 Q330 240 215 222 Q100 200 0 198Z" fill="url(#swooshRed)"/>
    <path d="M0 198 Q100 200 215 222 Q330 240 425 192 V250 H0Z" fill="#eeeeef"/>
    <circle cx="232" cy="162" r="34" fill="var(--red)" stroke="#fff" stroke-width="3"/>
    <text x="232" y="158" text-anchor="middle" font-family="Cabin, sans-serif" font-size="8.5" font-weight="700" fill="#fff">Environmental</text>
    <text x="232" y="170" text-anchor="middle" font-family="Cabin, sans-serif" font-size="8.5" font-weight="700" fill="#fff">Health Survey</text>
  </svg>

  <div class="brand"><span class="brand-mark"></span>Hollis College of Nursing</div>
  <h1 class="summary-title">EXECUTIVE<br>SUMMARY</h1>

  <div class="summary-body">
    <p>Environmental health is recognized as a core competency for nurses by the National Nurse Practice Council Standards of Professional Nursing Practice (2015). Marlow, Tate, Osei, &amp; Brandt (2007) found that the majority of nursing programs at both the graduate and undergraduate level do not include environmental health concepts in their curricula, leading to a lack of knowledge among providers for environmental concerns that relate to their patient population. The extent of environmental health knowledge among healthcare providers in Indiana is currently unknown.</p>
    <p>The overall aim of this project is to improve health outcomes relating to environmental health among patients in Indiana by addressing gaps in knowledge among healthcare providers in Indiana. The project will first assess environmental health knowledge among healthcare providers in Indiana via an evidence-based psychometrically evaluated environmental health awareness tool. Based on an analysis of the data providers will receive specific continuing education recommendations to fill their gaps in environmental health knowledge. The goal of this project is to bolster healthcare providers' environmental health knowledge by pinpointing exactly which areas they need further education in and offering targeted continuing education.</p>
    <p>This project takes a unique approach to provider education by choosing to offer specific recommendations based on an assessment tool rather than offering a broad educational package. By specifically targeting areas providers are less knowledgeable about this project adds value by reducing the amount of time spent by providers in reviewing materials they already know, and recognizing the value of the adult learner's current knowledge. According to Haverly (1991), ensuring that environmental concepts are included in a nurse's armamentarium will result in improved outcomes and a paradigm shift in population-focused interventions and preventive care.</p>
  </div>

  <div class="survey-pill">The survey link : <strong>http://shortlinkr.example/surveyquo</strong></div>
</section>

<section class="postcard" aria-label="Postcard">
  <svg class="postcard-art" viewBox="0 0 625 425" aria-hidden="true">
    <defs>
      <linearGradient id="bandRed" x1="0" y1="0" x2="1" y2="0">
        <stop offset="0" stop-color="#b0222f"/>
        <stop offset="1" stop-color="#c8303c"/>
      </linearGradient>
    </defs>
    <path d="M0 0 H262 Q318 200 278 425 H0Z" fill="#f4f4f5"/>
    <rect x="0" y="292" width="300" height="82" fill="url(#bandRed)"/>
    <path d="M262 0 H276 Q345 200 303 425 H278 Q318 200 262 0Z" fill="var(--red)"/>
  </svg>

  <div class="topics">
    <h2>DNP Project CE Topics</h2>
    <ul>
      <li><svg width="8" height="8" viewBox="0 0 8 8"><circle cx="4" cy="4" r="4" fill="#b0222f"/><path d="M3 2 L5 4 L3 6" stroke="#fff" stroke-width="1.2" fill="none"/></svg>General Environmental Health</li>
      <li><svg width="8" height="8" viewBox="0 0 8 8"><circle cx="4" cy="4" r="4" fill="#b0222f"/><path d="M3 2 L5 4 L3 6" stroke="#fff" stroke-width="1.2" fill="none"/></svg>Taking an Exposure History</li>
      <li><svg width="8" height="8" viewBox="0 0 8 8"><circle cx="4" cy="4" r="4" fill="#b0222f"/><path d="M3 2 L5 4 L3 6" stroke="#fff" stroke-width="1.2" fill="none"/></svg>Food Protection</li>
      <li><svg width="8" height="8" viewBox="0 0 8 8"><circle cx="4" cy="4" r="4" fill="#b0222f"/><path d="M3 2 L5 4 L3 6" stroke="#fff" stroke-width="1.2" fill="none"/></svg>Potable Water</li>
      <li><svg width="8" height="8" viewBox="0 0 8 8"><circle cx="4" cy="4" r="4" fill="#b0222f"/><path d="M3 2 L5 4 L3 6" stroke="#fff" stroke-width="1.2" fill="none"/></svg>Wastewater</li>
      <li><svg width="8" height="8" viewBox="0 0 8 8"><circle cx="4" cy="4" r="4" fill="#b0222f"/><path d="M3 2 L5 4 L3 6" stroke="#fff" stroke-width="1.2" fill="none"/></svg>Air Quality &amp; Environmental Noise</li>
      <li><svg width="8" height="8" viewBox="0 0 8 8"><circle cx="4" cy="4" r="4" fill="#b0222f"/><path d="M3 2 L5 4 L3 6" stroke="#fff" stroke-width="1.2" fill="none"/></svg>Housing Sanitation and Safety</li>
      <li><svg width="8" height="8" viewBox="0 0 8 8"><circle cx="4" cy="4" r="4" fill="#b0222f"/><path d="M3 2 L5 4 L3 6" stroke="#fff" stroke-width="1.2" fill="none"/></svg>Disaster Sanitation</li>
      <li><svg width="8" height="8" viewBox="0 0 8 8"><circle cx="4" cy="4" r="4" fill="#b0222f"/><path d="M3 2 L5 4 L3 6" stroke="#fff" stroke-width="1.2" fill="none"/></svg>Asbestos</li>
      <li><svg width="8" height="8" viewBox="0 0 8 8"><circle cx="4" cy="4" r="4" fill="#b0222f"/><path d="M3 2 L5 4 L3 6" stroke="#fff" stroke-width="1.2" fill="none"/></svg>Polychlorinated Biphenyls (PCBs) Toxicity</li>
      <li><svg width="8" height="8" viewBox="0 0 8 8"><circle cx="4" cy="4" r="4" fill="#b0222f"/><path d="M3 2 L5 4 L3 6" stroke="#fff" stroke-width="1.2" fill="none"/></svg>Environmental Triggers of Asthma</li>
      <li><svg width="8" height="8" viewBox="0 0 8 8"><circle cx="4" cy="4" r="4" fill="#b0222f"/><path d="M3 2 L5 4 L3 6" stroke="#fff" stroke-width="1.2" fill="none"/></svg>Nursing Focus: Clean Air, Climate, &amp; Health</li>
      <li><svg width="8" height="8" viewBox="0 0 8 8"><circle cx="4" cy="4" r="4" fill="#b0222f"/><path d="M3 2 L5 4 L3 6" stroke="#fff" stroke-width="1.2" fill="none"/></svg>Hydraulic Fracturing</li>
      <li><svg width="8" height="8" viewBox="0 0 8 8"><circle cx="4" cy="4" r="4" fill="#b0222f"/><path d="M3 2 L5 4 L3 6" stroke="#fff" stroke-width="1.2" fill="none"/></svg>Radon Exposure</li>
      <li><svg width="8" height="8" viewBox="0 0 8 8"><circle cx="4" cy="4" r="4" fill="#b0222f"/><path d="M3 2 L5 4 L3 6" stroke="#fff" stroke-width="1.2" fill="none"/></svg>“Greening” Healthcare &amp; Hospitals</li>
    </ul>
  </div>

  <div class="ce-links">
    <h3>CEs:</h3>
    <p>https://learn.healthmodules.example/ehs/ephoc</p>
    <p>http://toxcourses.example/csem/conteduc</p>
    <p>http://nurseclimate.example/pages/view/82102/advancing-clean<br>-air-climate-and-health-opportunities-for-nurses</p>
  </div>

  <div class="card-survey">The survey link : <strong>http://shortlinkr.example/surveyquo</strong></div>

  <div class="brand"><span class="brand-mark"></span>Hollis College of Nursing</div>
  <div class="stamp-box" aria-label="Postage area"></div>
  <div class="address-lines" aria-label="Address area"><span></span><span></span><span></span><span></span></div>
</section>

</body>
</html>
```